New Business Card Design

We would like to refresh our business cards and make them look better. We are an IT company specialising in Cloud Services, IT Managed Services, software and hardware. I have attached a PSD of our current design. Also attached our logo.
Updates

I have uploaded all new logos in EPS format.

Can you please edit all designs to include a job title for Marcus Hale, eg. General Manager

Industry/Entity Type

Software

Colors
ffffff

Requirements
Must have
• Please use white background.
Should not have
• Black background

```html
<!DOCTYPE html>
<html lang="en">
<head>
<meta charset="utf-8">
<title>Novaric Technology – Business Card</title>
<link rel="stylesheet" href="https://fonts.googleapis.com/css2?family=Source+Sans+3:wght@400;500&display=swap">
<style>
  :root {
    --paper: #ffffff;
    --card-edge: #cfcfcf;
    --ink-dark: #1b2a33;
    --accent-red: #c0392b;
    --link-blue: #2f6299;
    --rule: #222222;
    --faint-circle: #fbf1ee;
    --font-main: "Source Sans 3", "Myriad Pro", Arial, sans-serif;
  }
  * { box-sizing: border-box; margin: 0; padding: 0; }
  html, body {
    width: 1200px; height: 1000px; overflow: hidden;
    background: var(--paper);
    font-family: var(--font-main);
  }
  .stage { position: relative; width: 1200px; height: 1000px; }

  .card {
    position: absolute;
    width: 740px; height: 416px;
    background: var(--paper);
    border: 1px solid var(--card-edge);
    overflow: hidden;
  }
  .card--front { left: 66px; top: 52px; }
  .card--back  { left: 278px; top: 540px; }

  .brand { position: absolute; display: flex; align-items: center; }
  .brand__dot { border-radius: 50%; background: var(--accent-red); flex: none; }
  .brand__name { color: var(--ink-dark); font-weight: 400; white-space: nowrap; }

  .card--front .brand { left: 70px; top: 50px; }
  .card--front .brand__dot { width: 44px; height: 44px; margin-right: 14px; }
  .card--front .brand__name { font-size: 26px; letter-spacing: 2px; }

  .card--back .brand { left: 190px; top: 146px; }
  .card--back .brand__dot { width: 70px; height: 70px; margin-right: 22px; }
  .card--back .brand__name { font-size: 40px; letter-spacing: 4px; }

  .backdrop-circle {
    position: absolute; left: 460px; top: 115px;
    width: 250px; height: 250px; border-radius: 50%;
    background: var(--faint-circle);
  }

  .holder { position: absolute; right: 40px; top: 44px; text-align: right; }
  .holder__name { font-size: 44px; font-weight: 400; color: var(--ink-dark); line-height: 1; }
  .holder__title {
    margin-top: 4px; font-size: 14px; letter-spacing: 3px;
    text-transform: uppercase; color: var(--accent-red);
  }

  .divider {
    position: absolute; left: 37px; right: 37px; top: 271px;
    height: 1px; background: var(--rule);
  }

  .contact { position: absolute; list-style: none; }
  .contact--left  { left: 41px; top: 302px; }
  .contact--right { right: 38px; top: 302px; }
  .contact__item {
    display: flex; align-items: center; height: 26px; margin-bottom: 17px;
    font-size: 21px; color: var(--link-blue);
  }
  .contact__icon { width: 26px; height: 26px; margin-right: 11px; flex: none; }
</style>
</head>
<body>
<main class="stage">

  <section class="card card--front" aria-label="Business card front">
    <div class="backdrop-circle" aria-hidden="true"></div>

    <div class="brand">
      <span class="brand__dot" aria-hidden="true"></span>
      <span class="brand__name">Novaric Technology</span>
    </div>

    <div class="holder">
      <h1 class="holder__name">Marcus Hale</h1>
      <p class="holder__title">General Manager</p>
    </div>

    <div class="divider"></div>

    <ul class="contact contact--left">
      <li class="contact__item">
        <svg class="contact__icon" viewBox="0 0 26 26" aria-hidden="true">
          <circle cx="13" cy="13" r="13" fill="#c0392b"/>
          <path d="M8.5 7.5c1-1 2-.8 2.6.2l1 1.7c.4.7.2 1.4-.4 1.9l-.7.5c.6 1.5 1.8 2.8 3.3 3.4l.5-.7c.5-.6 1.2-.8 1.9-.4l1.7 1c1 .6 1.2 1.6.2 2.6-1 1-2.6 1.3-4.4.3-2.4-1.3-4.4-3.3-5.7-5.7-1-1.8-.7-3.4.3-4.4z" fill="#fff"/>
        </svg>
        07 3188 4410
      </li>
      <li class="contact__item">
        <svg class="contact__icon" viewBox="0 0 26 26" aria-hidden="true">
          <circle cx="13" cy="13" r="13" fill="#c0392b"/>
          <rect x="9" y="6" width="8" height="14" rx="1.5" fill="#fff"/>
          <rect x="10.3" y="8" width="5.4" height="8.5" fill="#c0392b"/>
          <circle cx="13" cy="18.2" r=".8" fill="#c0392b"/>
        </svg>
        0412 557 309
      </li>
    </ul>

    <ul class="contact contact--right">
      <li class="contact__item">
        <svg class="contact__icon" viewBox="0 0 26 26" aria-hidden="true">
          <circle cx="13" cy="13" r="13" fill="#c0392b"/>
          <rect x="6.5" y="8.5" width="13" height="9" rx="1" fill="#fff"/>
          <path d="M7 9l6 5 6-5" fill="none" stroke="#c0392b" stroke-width="1.3"/>
        </svg>
        mhale@novaricit.com.au
      </li>
      <li class="contact__item">
        <svg class="contact__icon" viewBox="0 0 26 26" aria-hidden="true">
          <circle cx="13" cy="13" r="13" fill="#c0392b"/>
          <g fill="none" stroke="#fff" stroke-width="1.3">
            <circle cx="13" cy="13" r="7"/>
            <ellipse cx="13" cy="13" rx="3" ry="7"/>
            <path d="M6 13h14M7 9.5h12M7 16.5h12"/>
          </g>
        </svg>
        novaricit.com.au
      </li>
    </ul>
  </section>

  <section class="card card--back" aria-label="Business card back">
    <div class="brand">
      <span class="brand__dot" aria-hidden="true"></span>
      <span class="brand__name">Novaric Technology</span>
    </div>
  </section>

</main>
</body>
</html>
```